Web Design Project - (DESIGN AND FOLLOW UP CODING)

Web design for new management consultancy company

**About The Hadley Collective

We work with organisations find and implement creative and sensible solutions...

We explore and inform…We have in-house research capability and enrich discussion through our own research, analysis and inputs. We interview staff and stakeholders, analyse data and literature and help you develop knowledge and solutions, and the plans to implement these.

We present new ideas…We develop proposals and reports that use internally and externally derived evidence to propose effective new solutions.

Specialties
Higher Education, TAFE, Local Government, Regional Development

Industry
Education Management
Updates

LOGO added to brief (or email me on mavenlink@quorix.com.au to get copy

Target Market(s)

Business and government managers

Industry/Entity Type

Education

Requirements
Must have
• Sections:

**About
We work with organisations find and implement solutions to opportunities and challenges.
We explore and inform…
We present new ideas…

We develop proposals and reports that link internally and externally derived evidence to develop and implement new solutions.

Our three practice pillars are-
Ideas and partnerships:
Knowledgeable leaders:
Solutions:

** People
Marcus Pellow (PHOTO) Bio

** Services
Acumen - Solutions - Partnerships -Implementation
- On time and within budget.
- Project leadership.
- Researched inputs and facilitated outcomes.
- Focus on implementation.
- Develop value-adding partnerships and get them funded
- Creative responses to funding opportunities
- Organisational reviews

Sectors
-Education
-State Government
- Local Government
- Utilities
- Financial services
- Health and ageing
- Human services
- Government
-Regional

** Careers

** Key Partners
With weblinks

** Contact

Links to Twitter LinkedIn Facebook
Nice to have
• Logo available from: mavenlink@quorix.com.au

```html
<!DOCTYPE html>
<html lang="en">
<head>
<meta charset="utf-8">
<title>The Hadley Collective</title>
<link href="https://fonts.googleapis.com/css2?family=Arimo:wght@400;700&display=swap" rel="stylesheet">
<style>
  :root {
    --page-blue: #0b5a86;
    --paper: #ffffff;
    --brand-blue: #1c5f8c;
    --accent: #f58a1f;
    --accent-dark: #e0761a;
    --ink: #111111;
    --body: #6b6b6b;
    --label: #6a6a6a;
    --rule: #dedede;
    --hero-a: #7a5a38;
    --hero-b: #c98a4c;
  }
  * { box-sizing: border-box; margin: 0; padding: 0; }
  html, body { width: 803px; height: 1200px; overflow: hidden; }
  body { background: var(--page-blue); font-family: "Arimo", Arial, sans-serif; color: var(--body); }
  .page { position: absolute; left: 62px; top: 0; width: 680px; height: 1200px; background: var(--paper); overflow: hidden; }
  .abs { position: absolute; }

  .brand { left: 28px; top: 16px; display: flex; align-items: center; gap: 6px; }
  .brand-mark { width: 16px; height: 16px; background: var(--accent); flex: none; }
  .brand-name { font-size: 13.5px; font-weight: 700; color: var(--brand-blue); text-transform: uppercase; white-space: nowrap; }

  .nav a { position: absolute; top: 16px; font-size: 8px; line-height: 20px; text-transform: uppercase; color: #333; text-decoration: none; white-space: nowrap; }
  .nav a.current { background: var(--accent); color: #fff; border: 1px solid var(--accent-dark); border-radius: 2px; width: 47px; text-align: center; }

  .hero { left: 28px; top: 62px; width: 624px; height: 283px; background: linear-gradient(160deg, #d8c09a 0%, var(--hero-b) 40%, var(--hero-a) 100%); }

  .rule { height: 1px; background: var(--rule); }

  .section-title { display: flex; align-items: center; gap: 7px; font-size: 16px; font-weight: 400; color: var(--ink); text-transform: uppercase; white-space: nowrap; }
  .section-title.small { font-size: 11px; gap: 4px; }

  .service-list { list-style: none; width: 170px; }
  .service-list li { font-size: 7.5px; line-height: 10px; padding: 5px 0 7px; border-bottom: 1px solid var(--rule); }
  .service-list li:last-child { border-bottom: none; }
  .service-list a { color: var(--accent); }

  .btn { display: block; width: 59px; height: 25px; background: var(--accent); border: 1px solid var(--accent-dark); border-radius: 2px; color: #fff; font-size: 7.5px; text-align: center; line-height: 23px; text-decoration: underline; box-shadow: 0 1px 2px rgba(0,0,0,.2); }

  .partner { width: 170px; height: 64px; border-bottom: 1px solid var(--rule); display: flex; gap: 11px; }
  .partner + .partner { padding-top: 0; }
  .partner-photo { width: 44px; height: 44px; background: linear-gradient(135deg, #b8b8b8, #6d6d6d); flex: none; }
  .partner-text { font-size: 7.5px; line-height: 14px; color: var(--body); }
  .partner-text strong { color: var(--label); }
  .partner-text a { color: var(--accent); }

  .copy { font-size: 7.5px; line-height: 13.6px; color: var(--body); }
  .copy h4 { font-size: 7.5px; font-weight: 700; color: var(--label); }
  .copy p { margin-bottom: 7px; }
  .pillar-photo { float: left; width: 205px; height: 136px; margin: 0 17px 4px 0; background: linear-gradient(120deg, #f2f2f2, #9a9a9a 55%, #3a3a3a); }

  .sector-list { list-style: none; font-size: 7.5px; text-transform: uppercase; color: var(--label); font-weight: 700; }
  .sector-list li { height: 21px; }
  .sector-list a { color: var(--accent); font-weight: 400; text-transform: none; text-decoration: none; }
  .about-head { font-size: 8.5px; font-weight: 700; color: var(--ink); }
  .about-more { color: var(--accent); font-size: 7.5px; text-decoration: none; }

  .social { left: 281px; top: 1108px; display: flex; gap: 12px; }
  .social span { display: block; width: 32px; height: 32px; border-radius: 50%; background: radial-gradient(circle at 40% 35%, #ffb25a, var(--accent) 60%, #c8600e); box-shadow: 0 3px 4px rgba(0,0,0,.25); }
  .copyright { left: 0; width: 680px; top: 1157px; text-align: center; font-size: 7px; color: var(--body); }
</style>
</head>
<body>
<div class="page">
  <header>
    <div class="abs brand"><span class="brand-mark"></span><span class="brand-name">The Hadley Collective</span></div>
    <nav class="nav">
      <a class="current" href="#" style="left:262px">Home</a>
      <a href="#" style="left:320px">About</a>
      <a href="#" style="left:369px">People</a>
      <a href="#" style="left:421px">Services</a>
      <a href="#" style="left:482px">Careers</a>
      <a href="#" style="left:541px">Partners</a>
      <a href="#" style="left:604px">Contact</a>
    </nav>
  </header>

  <div class="abs hero" role="img" aria-label="Boardroom with a long timber table and leather chairs"></div>
  <div class="abs rule" style="left:28px;top:370px;width:624px"></div>

  <h2 class="abs section-title" style="left:28px;top:397px">
    <svg width="16" height="18" viewBox="0 0 16 18"><rect x="1" y="1" width="14" height="16" rx="2" fill="none" stroke="#111" stroke-width="1.6"/><path d="M4 6h8M4 9h8M4 12h8" stroke="#111" stroke-width="1.4"/></svg>
    Services
  </h2>
  <ul class="abs service-list" style="left:28px;top:427px">
    <li><a href="#">On time and within budget</a></li>
    <li><a href="#">Project leadership</a></li>
    <li><a href="#">Researched inputs and facilitated outcomes</a></li>
    <li><a href="#">Focus on implementation</a></li>
    <li><a href="#">evelop value-adding partnerships and get them funded</a></li>
    <li><a href="#">Creative responses to funding opportunities</a></li>
    <li><a href="#">Organisational reviews</a></li>
  </ul>
  <a class="abs btn" href="#" style="left:28px;top:608px">Read More</a>

  <h2 class="abs section-title" style="left:28px;top:660px">
    <svg width="16" height="18" viewBox="0 0 16 18"><rect x="1" y="1" width="14" height="16" rx="2" fill="none" stroke="#111" stroke-width="1.6"/><path d="M4 6h8M4 9h8M4 12h8" stroke="#111" stroke-width="1.4"/></svg>
    Key Partners
  </h2>
  <div class="abs" style="left:28px;top:698px">
    <div class="partner"><div class="partner-photo" role="img" aria-label="Partner 1 photo"></div><div class="partner-text"><strong>Partner 1:</strong><br>Donec mattis libero eget urna.<br><a href="#">weblink</a></div></div>
    <div class="partner" style="padding-top:0;height:64px"><div class="partner-photo" role="img" aria-label="Partner 2 photo" style="background:linear-gradient(135deg,#d8c36a,#3d3d3d);margin-top:0"></div><div class="partner-text"><strong>Partner 2:</strong><br>Donec mattis libero eget urna.<br><a href="#">weblink</a></div></div>
    <div class="partner" style="border-bottom:none"><div class="partner-photo" role="img" aria-label="Partner 3 photo" style="background:linear-gradient(135deg,#c9c9c9,#7f7f7f)"></div><div class="partner-text"><strong>Partner 3:</strong><br>Donec mattis libero eget urna.<br><a href="#">weblink</a></div></div>
  </div>
  <a class="abs btn" href="#" style="left:28px;top:887px">Read More</a>

  <h2 class="abs section-title" style="left:226px;top:397px">
    <svg width="16" height="18" viewBox="0 0 16 18"><rect x="1" y="1" width="14" height="16" rx="2" fill="none" stroke="#111" stroke-width="1.6"/><path d="M4 6h8M4 9h8M4 12h8" stroke="#111" stroke-width="1.4"/></svg>
    Our three practice pillars are:
  </h2>
  <div class="abs copy" style="left:226px;top:432px;width:426px">
    <div class="pillar-photo" role="img" aria-label="Black and white photo of a handshake"></div>
    <h4>Ideas and partnerships:</h4>
    <p>Lorem ipsum dolor sit amet, consectetur adipiscing elit. In enim tortor, ultricies vitae dolor vitae, sagittis consequat quam. Nulla egestas sagittis lectus at varius. Aliquam convallis pretium consectetur. Nam vitae justo eget risus fermentum tincidunt ut ut lacus. Suspendisse arcu urna, dictum eu vehicula sit amet, sagittis non lectus. Vivamus at mi a ligula elementum suscipit. Sed consequat pretium auctor.</p>
    <h4>Knowledgeable leaders:</h4>
    <p>Ut gravida lectus quis cursus tempus. Cras a nisi ac diam tristique egestas ac euismod nibh. Praesent eros turpis, blandit nec malesuada quis, suscipit vel turpis. Ut consequat lorem in auctor suscipit. Integer rhoncus, mauris id tincidunt luctus, enim metus malesuada quam, eu blandit neque eros in justo. Lorem ipsum dolor sit amet, consectetur adipiscing elit. Vestibulum blandit, odio eu ultricies porta, lectus justo porttitor risus, a vehicula nisl urna sed felis. Nulla facilisi. Curabitur ornare tortor ac felis consequat, in mattis lectus malesuada. Morbi at aliquam nulla, non condimentum neque. Sed non nunc consequat, interdum libero quis, gravida enim.</p>
    <h4>Solutions:</h4>
    <p>Phasellus et ipsum ornare mauris auctor vestibulum. Nam sodales tempor ante, laoreet fringilla mi euismod non. Praesent in ligula sit amet odio rhoncus volutpat id in dui. Class aptent taciti sociosqu ad litora torquent per conubia nostra, per inceptos himenaeos. Aenean non lacinia orci, eget porttitor elit. Praesent mollis condimentum ante id ullamcorper. Donec elementum diam erat, eget porta ante gravida et. Donec id turpis nibh. Ut sollicitudin ligula dolor. Maecenas vulputate, felis non suscipit mollis, leo erat semper purus, eu auctor elit mauris nec lectus. Nam quis varius urna.</p>
  </div>
  <a class="abs btn" href="#" style="left:226px;top:752px">Read More</a>
  <div class="abs rule" style="left:226px;top:800px;width:426px"></div>

  <h3 class="abs section-title small" style="left:226px;top:822px">
    <svg width="9" height="10" viewBox="0 0 9 10"><rect x=".6" y=".6" width="7.8" height="8.8" fill="none" stroke="#111" stroke-width="1"/><path d="M2 3.5h5M2 5h5M2 6.5h5" stroke="#111" stroke-width=".8"/></svg>
    Sectors
  </h3>
  <ul class="abs sector-list" style="left:226px;top:855px">
    <li>Education <a href="#">Read More&gt;</a></li>
    <li>State Government <a href="#">Read More&gt;</a></li>
    <li>Local Government <a href="#">Read More&gt;</a></li>
    <li>Utilities <a href="#">Read More&gt;</a></li>
    <li>Financial Services <a href="#">Read More&gt;</a></li>
    <li>Health and Ageing <a href="#">Read More&gt;</a></li>
    <li>Human Services <a href="#">Read More&gt;</a></li>
    <li>Government <a href="#">Read More&gt;</a></li>
    <li>Regional <a href="#">Read More&gt;</a></li>
  </ul>

  <h3 class="abs section-title small" style="left:453px;top:822px">
    <svg width="9" height="10" viewBox="0 0 9 10"><rect x=".6" y=".6" width="7.8" height="8.8" fill="none" stroke="#111" stroke-width="1"/><path d="M2 3.5h5M2 5h5M2 6.5h5" stroke="#111" stroke-width=".8"/></svg>
    About Us
  </h3>
  <div class="abs about-head" style="left:453px;top:853px">LOREM IPSUM</div>
  <div class="abs copy" style="left:453px;top:868px;width:200px">
    <p>Lorem ipsum dolor sit amet, consectetur adipiscing elit. In enim tortor, ultricies vitae dolor vitae, sagittis consequat quam. Nulla egestas sagittis lectus at varius. Aliquam convallis pretium consectetur. Nam vitae justo eget risus fermentum tincidunt ut ut lacus. Suspendisse arcu urna, dictum eu vehicula sit amet, sagittis non lectus. Vivamus at mi a ligula elementum suscipit. Sed consequat pretium auctor...</p>
    <a class="about-more" href="#">Read More&gt;&gt;</a>
  </div>

  <div class="abs rule" style="left:28px;top:1073px;width:624px"></div>
  <div class="abs social" aria-label="Social links"><span role="img" aria-label="Social link 1"></span><span role="img" aria-label="Social link 2"></span><span role="img" aria-label="Social link 3"></span></div>
  <p class="abs copyright">Copyright (c) 2013 Hadley Collective. All rights reserved.</p>
</div>
</body>
</html>
```